Broschüre für Toben – Tollen – Balancieren
Zielgruppe
Wir bieten Rangel und Raufkurse für Kinder ab dem Vorschulalter bis zu weiterführenden Schulen. Die Broschüre erhalten Lehrer, Erzieher und Direktoren der Einrichtungen an denen die Kurse Angeboten werden.
Aufgabenstellung
Design sollte eher Schlicht und modern wirken und an der homepage
www.boden-lernwerk.de orientiert sein.
Infobroschüre zum Durchblättern, kein Folder. Seitenfolge wie auf der Powerpoint präsentation.

```html
<!DOCTYPE html>
<html lang="de">
<head>
<meta charset="utf-8">
<title>Toben – Tollen – Balancieren · Broschüre Seite 2–3</title>
<link href="https://fonts.googleapis.com/css2?family=Open+Sans:wght@400;600;700;800&display=swap" rel="stylesheet">
<style>
  :root {
    --bg: #dcdcdc;
    --paper: #ffffff;
    --ink: #3a3a3a;
    --ink-strong: #262626;
    --brand-red: #a3161a;
    --muted: #6b6b6b;
  }
  * { box-sizing: border-box; margin: 0; padding: 0; }
  html, body {
    width: 1200px; height: 833px; overflow: hidden;
    background: var(--bg);
    font-family: "Open Sans", Arial, sans-serif;
    color: var(--ink);
  }
  .spread {
    position: absolute; left: 60px; top: 40px;
    width: 1080px; height: 753px;
    display: flex;
    box-shadow: 0 10px 30px rgba(0,0,0,.18);
  }
  .page { position: relative; width: 540px; height: 753px; background: var(--paper); overflow: hidden; }

  /* left page: photo */
  .photo {
    position: absolute; inset: 0;
    background:
      linear-gradient(180deg, rgba(0,0,0,0) 60%, rgba(10,20,40,.35) 100%),
      linear-gradient(125deg, #9c3b2c 0%, #8a3426 35%, #3f4f78 62%, #2b3a63 80%, #8a8e96 100%);
  }
  .photo-caption {
    position: absolute; left: 40px; bottom: 50px; width: 290px;
    color: #fff; font-weight: 700; font-size: 12.5px; line-height: 1.55;
  }

  /* right page */
  .article { position: absolute; left: 52px; top: 112px; right: 40px; }
  .headline {
    color: var(--brand-red); font-weight: 700;
    font-size: 27px; line-height: 1.15;
    max-width: 400px;
  }
  .headline-rule { width: 34px; height: 3px; background: var(--brand-red); margin: 16px 0 14px; }
  .lead {
    font-weight: 700; font-size: 12.5px; line-height: 1.5; color: var(--ink-strong);
  }
  .dropcap {
    float: left; font-size: 44px; line-height: 38px; font-weight: 800;
    margin: 2px 8px 0 0; color: var(--ink-strong);
  }
  .body-columns {
    margin-top: 16px;
    display: grid; grid-template-columns: 1fr 1fr; column-gap: 22px;
    font-size: 10px; line-height: 1.6; color: var(--ink);
    text-align: justify; hyphens: auto;
  }
  .body-columns p + p { margin-top: 12px; }

  .info-box {
    margin-top: 22px;
    background: var(--brand-red); color: #fff;
    border-radius: 6px; padding: 14px 14px 16px;
    font-size: 10px; line-height: 1.6; text-align: left;
  }
  .info-box h3 { font-size: 10.5px; font-weight: 700; margin-bottom: 4px; }
  .info-box .icon { display: inline-block; vertical-align: -1px; margin-right: 6px; }

  .page-footer .brand {
    position: absolute; left: 52px; bottom: 30px;
    font-size: 11px; font-weight: 700; letter-spacing: .5px; color: var(--ink-strong);
  }
  .page-footer .folio {
    position: absolute; right: 40px; bottom: 60px;
    font-size: 9px; letter-spacing: .8px; color: var(--muted);
    padding-right: 10px; border-right: 1px solid var(--muted);
    line-height: 26px;
  }
  .gutter-shade {
    position: absolute; left: 540px; top: 0; width: 40px; height: 753px;
    background: linear-gradient(90deg, rgba(0,0,0,.12), rgba(0,0,0,0));
    pointer-events: none;
  }
</style>
</head>
<body>
<main class="spread">
  <section class="page page-left">
    <div class="photo" role="img" aria-label="Foto: zwei Jungen rangeln spielerisch vor einer roten Backsteinmauer, eine erwachsene Hand greift schlichtend ein"></div>
    <p class="photo-caption">In der heutigen Zeit scheint es Eltern und Erziehungspersonen schwer zu fallen, den richtigen Mittelweg für die Erziehung der nächsten Generation zu finden.</p>
  </section>

  <section class="page page-right">
    <article class="article">
      <h1 class="headline">Rangeln und Raufen ist eine Urform der kindlichen Bewegung</h1>
      <div class="headline-rule"></div>
      <p class="lead"><span class="dropcap">W</span>enn man Kindern zu viel Freiraum lässt, machen sie oftmals genau das, was Erwachsene dann als „falsch“ einstufen. Sie raufen, streiten, rebellieren. Doch ist es der richtige Weg, dieses Verhalten bedingungslos zu unterbinden?</p>
      <div class="body-columns">
        <div class="column column-left">
          <p>Schließlich sind es Verhaltensweisen, die Kinder gerade dann aufzeigen, wenn sie unter sich sind, wenn sie sich uneingeschränkt bewegen dürfen, wenn sie Kind sein dürfen. Rangeln und Raufen liegt in der menschlichen Natur. Es ist eine Urform der kindlichen Bewegung, Streit ist ein soziales Phänomen, das überall existiert und nicht zu vermeiden ist.</p>
          <p>Wenn man von Menschen erwartet, dass sie Konflikte fair und friedlich lösen, darf ihnen im Kindesalter das Streiten nicht verwehrt bleiben. Kinder die lernen, spielerisch und friedlich miteinander zu raufen, tun das, was ihrer kindlichen Neugierde entspricht. Sie erforschen die Kräfte ihres Körpers und testen ihre Grenzen.</p>
        </div>
        <div class="column column-right">
          <p>Sie haben Spaß, dürfen austeilen und müssen einstecken. All das in einem friedlichen Umfeld, das klare Regeln festlegt und in dem die Kinder, statt zu blindem Gehorsam, zu Respekt und Selbstdisziplin motiviert werden.</p>
          <aside class="info-box">
            <h3>Eine gesunde Richtung vorgeben</h3>
            <p><svg class="icon" width="14" height="10" viewBox="0 0 14 10" aria-hidden="true"><path d="M7 0 14 3 7 6 0 3Z" fill="#fff"/><path d="M3 4.5v3c1 1.3 7 1.3 8 0v-3L7 6.3Z" fill="#fff"/></svg>Kinder, die auch mal rebellisch sind, entwickeln sich zu selbstständigen Menschen, die ihrem persönlichen Glück folgen. Es ist unsere tiefe Überzeugung, dass unser Kampfsport diese kindlichen Eigenschaften in eine gesunde Richtung lenken kann.</p>
          </aside>
        </div>
      </div>
    </article>

    <footer class="page-footer">
      <span class="brand">BODENLERNWERK</span>
      <span class="folio">SEITE 3</span>
    </footer>
  </section>
  <div class="gutter-shade"></div>
</main>
</body>
</html>
```